Business Card Design for a Lending Business (Hard Money loans)

We need a business card for our Real Estate Lending business. We do hard Money loans for real estate investors. We have an existing logo we like, see attached. I'd like the business card to mostly include the logo colors, but a bright color pop of some sort would be nice to see also. Card should include Logo, Company Name, Company Address, Employee Name, Cell Phone, Main Phone, Email, Website

Industry/Entity Type

Finance / Lending

Contact Information for Business Card

Logo, Company Name, Company Address, Employee Name, Cell Phone, Main Phone, Email, Website

Requirements
Nice to have
• I'd like the business card to mostly include the logo colors, but a bright color pop of some sort would be nice to see also.

```html
<!DOCTYPE html>
<html lang="en">
<head>
<meta charset="utf-8">
<title>Harborline Capital – Business Card</title>
<link rel="stylesheet" href="https://fonts.googleapis.com/css2?family=Arimo:wght@400;700&display=swap">
<style>
  :root {
    --backdrop: #d8dee1;
    --paper: #f7f7f6;
    --navy: #0a2389;
    --navy-deep: #05186a;
    --cyan: #1aa7df;
    --ink: #4a4a4a;
    --edge: #1a8fd0;
  }
  * { box-sizing: border-box; margin: 0; padding: 0; }
  html, body {
    width: 1200px; height: 1022px; overflow: hidden;
    background: var(--backdrop);
    font-family: "Arimo", Arial, sans-serif;
  }
  .sheet {
    width: 1200px; height: 1022px;
    display: flex; flex-direction: column; align-items: center; justify-content: center;
    gap: 60px;
  }
  .card {
    position: relative;
    width: 620px; height: 354px;
    border-bottom: 3px solid var(--edge);
    box-shadow: 0 12px 28px rgba(40, 50, 60, 0.22);
  }
  .card--front { background: var(--paper); color: var(--ink); }
  .card--back {
    background: radial-gradient(ellipse at 45% 40%, var(--navy) 0%, var(--navy-deep) 100%);
    display: flex; align-items: center; justify-content: center;
  }
  .holder { position: absolute; left: 46px; top: 42px; }
  .holder__name {
    color: var(--cyan); font-weight: 700; font-size: 20px; letter-spacing: 0.3px;
    text-transform: uppercase;
  }
  .holder__role { font-size: 14px; margin-top: 3px; }
  .contact {
    position: absolute; left: 46px; bottom: 40px;
    list-style: none; font-size: 14px; line-height: 20px;
  }
  .contact li { display: flex; align-items: center; gap: 10px; }
  .contact svg { width: 13px; height: 13px; flex: none; }
  .brand {
    position: absolute; right: 46px; top: 130px;
    display: flex; align-items: center; gap: 10px;
  }
  .brand__mark { width: 18px; height: 18px; border-radius: 50%; background: var(--cyan); }
  .brand__name { font-weight: 700; font-size: 24px; letter-spacing: 1px; color: var(--navy); text-transform: uppercase; }
  .address {
    position: absolute; right: 46px; bottom: 36px;
    font-size: 14px; line-height: 19px; text-align: left;
  }
  .card--back .brand { position: static; }
  .card--back .brand__mark { width: 26px; height: 26px; }
  .card--back .brand__name { color: #ffffff; font-size: 36px; letter-spacing: 2px; }
</style>
</head>
<body>
  <main class="sheet">
    <section class="card card--front">
      <div class="holder">
        <p class="holder__name">Marissa Kowalczyk</p>
        <p class="holder__role">Loan Coordinator</p>
      </div>

      <div class="brand">
        <span class="brand__mark"></span>
        <span class="brand__name">Harborline Capital</span>
      </div>

      <ul class="contact">
        <li>
          <svg viewBox="0 0 16 16" aria-hidden="true"><path fill="#1aa7df" d="M4 1l3 3-2 2c1 2 3 4 5 5l2-2 3 3-2 3C7 15 1 9 1 3z"/></svg>
          410-555-0148
        </li>
        <li>
          <svg viewBox="0 0 16 16" aria-hidden="true"><rect x="1" y="3" width="14" height="10" fill="none" stroke="#1aa7df" stroke-width="1.6"/><path d="M1 3l7 6 7-6" fill="none" stroke="#1aa7df" stroke-width="1.6"/></svg>
          hello@HarborlineCapital.com
        </li>
        <li>
          <svg viewBox="0 0 16 16" aria-hidden="true"><g fill="none" stroke="#1aa7df" stroke-width="1.2"><circle cx="8" cy="8" r="6.5"/><ellipse cx="8" cy="8" rx="3" ry="6.5"/><path d="M1.5 8h13M2.5 4.5h11M2.5 11.5h11"/></g></svg>
          www.HarborlineCapital.com
        </li>
      </ul>

      <address class="address" style="font-style: normal;">
        1250 Millbrook Lane<br>
        Fallston, MD 21047
      </address>
    </section>

    <section class="card card--back">
      <div class="brand">
        <span class="brand__mark"></span>
        <span class="brand__name">Harborline Capital</span>
      </div>
    </section>
  </main>
</body>
</html>
```